Revamp Marketing Website For Video Production Website

need to revamp current website www.quillhavenfilmworks.com
reference sites www.vandeo.com & http://layoutpike.com/quill/
Use all current content on current quill website. I want a revamped modenr look. Sometbing that wows customers.
reference site www.vandeo.com
Target Market(s)
business owners
Industry/Entity Type
Video Production
Number of Pages Required
5+ page
Colors
Designer to choose colors to be used in the design.
Requirements
Must have
- need to revamp current website www.quillhavenfilmworks.com
- reference sites www.vandeo.com & http://layoutpike.com/quill/
- Use all current content on current quill website. I want a revamped modenr look. Sometbing that wows customers.
- reference site www.vandeo.com
Nice to have
Should not have

```html
<!DOCTYPE html>
<html lang="en">
<head>
<meta charset="utf-8">
<title>Quill — Marketing Videos Made For You</title>
<link href="https://fonts.googleapis.com/css2?family=Raleway:wght@400;500;600;700;800&display=swap" rel="stylesheet">
<style>
:root{
  --navy:#0a2470;
  --navy-deep:#061a55;
  --blue:#0d3fa8;
  --cyan:#1aa7ec;
  --cyan-bright:#27c1f5;
  --ice:#e9f6fd;
  --ink:#1b2233;
  --muted:#5d6577;
  --white:#ffffff;
  --band:#0f1f57;
}
*{box-sizing:border-box;margin:0;padding:0}
html,body{width:1200px;height:4433px;overflow:hidden}
body{font-family:"Raleway",sans-serif;color:var(--ink);background:var(--white);position:relative}
a{text-decoration:none;color:inherit}
.btn{display:inline-flex;align-items:center;gap:8px;background:var(--cyan);color:var(--white);font-weight:700;font-size:13px;padding:12px 24px;border-radius:30px;box-shadow:0 6px 14px rgba(26,167,236,.35);white-space:nowrap}
.btn::before{content:"";width:0;height:0;border-left:6px solid var(--white);border-top:4px solid transparent;border-bottom:4px solid transparent}
.plain::before{display:none}

/* section divider band */
.band{position:absolute;left:0;width:1200px;height:40px;background:var(--band)}

/* hero */
.hero{position:absolute;top:0;left:0;width:1200px;height:640px;background:linear-gradient(120deg,var(--navy-deep) 0%,var(--blue) 70%,#1657c9 100%);overflow:hidden}
.topbar{position:absolute;top:26px;left:154px;width:896px;display:flex;align-items:center;justify-content:space-between}
.brand{display:flex;align-items:center;gap:10px;color:var(--white)}
.brand-mark{width:22px;height:22px;border-radius:50%;background:var(--cyan)}
.brand-name{font-weight:800;font-size:26px;letter-spacing:3px;line-height:1}
.brand-tag{font-size:8px;letter-spacing:1px;font-weight:600;margin-top:4px}
.nav{display:flex;gap:28px;font-size:11px;color:var(--white);align-items:center}
.nav .active{color:var(--cyan-bright);border-bottom:2px solid var(--cyan-bright);padding-bottom:3px}
.nav .auth{display:flex;gap:10px;margin-left:10px}
.nav .auth span{padding:6px 18px;border-radius:14px;border:1.5px solid var(--white)}
.nav .auth .login{background:var(--cyan);border-color:var(--cyan)}
.hero-copy{position:absolute;top:212px;left:154px;color:var(--white)}
.hero-copy h1{font-size:40px;font-weight:800;line-height:1.3}
.hero-copy h1 em{font-style:normal;color:var(--cyan-bright)}
.hero-cta{display:flex;align-items:center;gap:22px;margin-top:26px;font-size:13px}
.hero-cta u{color:var(--cyan-bright)}
.hero-photo{position:absolute;top:198px;left:640px;width:410px;height:262px;background:linear-gradient(135deg,#6d8fb4,#2d4f7c 60%,#c2a38a);border-radius:0 70px 0 70px}
.play{position:absolute;width:42px;height:42px;border-radius:50%;background:var(--cyan);border:4px solid var(--white);display:flex;align-items:center;justify-content:center}
.play::after{content:"";border-left:11px solid var(--white);border-top:7px solid transparent;border-bottom:7px solid transparent;margin-left:3px}
.hero .band{transform:rotate(-13deg);transform-origin:left top;top:600px;left:-30px;width:1320px}
.chevrons{position:absolute;top:570px;left:585px}

/* promote */
.promote{position:absolute;top:700px;left:0;width:1200px;height:440px}
.collage{position:absolute;left:154px;top:10px;width:450px;height:400px}
.collage .a{position:absolute;left:0;top:0;width:220px;height:400px;background:linear-gradient(180deg,#d8d2cc,#c04a55 55%,#8b8b93);border-radius:0 0 0 40px}
.collage .b{position:absolute;left:225px;top:25px;width:200px;height:270px;background:linear-gradient(180deg,#e7e3de,#d6b4ad 60%,#4a4c55)}
.collage .c{position:absolute;left:290px;top:295px;width:160px;height:105px;background:linear-gradient(135deg,var(--navy),var(--blue));border-radius:0 0 40px 0;display:flex;align-items:center;justify-content:center}
.collage .c i{width:26px;height:26px;border:2px solid var(--white);border-radius:50%;color:var(--white);font-style:normal;text-align:center;line-height:21px;font-size:18px}
.collage .play{left:428px;top:130px;width:34px;height:34px;border-width:3px}
.block h2{font-size:28px;font-weight:800;color:var(--navy);margin:14px 0 10px;line-height:1.2}
.flag{display:inline-block;width:16px;height:12px;background:var(--navy);border-radius:2px}
.sub{color:var(--cyan);font-size:14px;font-weight:600;display:flex;align-items:center;gap:8px}
.sub::before{content:"";width:42px;height:2px;background:var(--cyan);flex:none}
.block p{font-size:11px;line-height:1.7;color:var(--muted);margin:10px 0 22px}
.block p b{color:var(--navy)}
.promote .block{position:absolute;left:686px;top:80px;width:364px}
.award{position:absolute;top:1160px;left:0;width:1200px;height:440px}
.award .block{position:absolute;left:154px;top:125px;width:400px}
.social-cluster{position:absolute;left:585px;top:10px;width:470px;height:400px;border-radius:40px;background:linear-gradient(135deg,#2c4f99 0%,#c53d7e 45%,#d84a3a 70%,#2fb9d9 100%)}

/* portfolio */
.portfolio{position:absolute;top:1675px;left:0;width:1200px;height:525px;background:var(--navy)}
.section-title{font-size:30px;font-weight:800;text-align:center}
.portfolio .section-title{color:var(--white);padding-top:48px}
.cards{position:absolute;left:154px;top:120px;width:896px;display:flex;justify-content:space-between}
.pcard{width:290px;text-align:center;color:var(--white)}
.pcard .thumb{position:relative;height:220px;border-radius:0 50px 0 50px}
.pcard .thumb span{position:absolute;left:20px;right:20px;top:112px;font-size:13px;font-weight:800;line-height:1.3;text-shadow:0 1px 3px rgba(0,0,0,.6)}
.pcard .thumb .play{left:124px;top:172px}
.pcard .heart,.pcard .share{position:absolute;right:10px;width:22px;height:22px;border-radius:50%}
.pcard .heart{top:10px;background:#e0404f}
.pcard .share{top:38px;background:#2f6fd6}
.pcard h3{font-size:15px;font-weight:700;margin-top:38px}
.portfolio .center{position:absolute;left:0;right:0;top:450px;text-align:center}

/* features */
.features{position:absolute;top:2240px;left:0;width:1200px;height:770px;background:var(--ice)}
.features .section-title{color:var(--navy);padding-top:62px}
.fgrid{position:absolute;left:154px;top:135px;width:896px;display:grid;grid-template-columns:repeat(3,290px);justify-content:space-between;row-gap:50px}
.fcard{height:220px;background:var(--white);border-radius:0 40px 0 40px;padding:22px 24px;text-align:center;position:relative;box-shadow:0 6px 18px rgba(10,36,112,.08)}
.fcard h3{font-size:16px;font-weight:700;color:var(--navy)}
.fcard .tag{color:var(--cyan);font-size:12px;font-weight:600;margin:6px 0 8px;line-height:1.3}
.fcard p{font-size:9.5px;line-height:1.6;color:var(--muted)}
.fcard .more{display:block;font-size:8px;color:var(--cyan);margin-top:10px;letter-spacing:1px}
.fcard .ico{position:absolute;left:50%;bottom:-18px;width:36px;height:36px;margin-left:-18px;border-radius:50%;background:var(--cyan);border:4px solid var(--white)}
.fcard.dark{background:var(--navy)}
.fcard.dark h3,.fcard.dark p{color:var(--white)}
.fcard.dark .tag{color:var(--cyan-bright)}
.features .center{position:absolute;left:0;right:0;top:690px;text-align:center}

/* sizes */
.sizes{position:absolute;top:3010px;left:0;width:1200px;height:1030px}
.sizes .section-title{color:var(--navy);padding-top:50px}
.srow{position:absolute;left:154px;width:896px;display:flex;gap:22px;align-items:center}
.stext{width:230px;flex:none;font-size:11px;line-height:1.7;color:var(--muted)}
.stext b{color:var(--navy)}
.stext .hl{color:var(--cyan)}
.shot{position:relative;flex:1;border-radius:0 40px 0 40px}
.shot span{position:absolute;left:12px;bottom:14px;background:var(--navy);color:var(--white);font-size:12px;font-weight:800;padding:4px 10px}
.sizes .center{position:absolute;left:0;right:0;top:955px;text-align:center}

/* footer */
.footer{position:absolute;top:4080px;left:0;width:1200px;height:353px;background:var(--navy);color:var(--white)}
.fcol{position:absolute;top:55px}
.fcol h4{font-size:15px;font-weight:700;margin-bottom:22px}
.fcol p{font-size:10px;line-height:1.8}
.fcol .strong{font-weight:700;font-size:11px;margin:16px 0 6px}
.fcol .hl{color:var(--cyan)}
.dots{display:flex;gap:8px;margin-top:14px}
.dots i{width:20px;height:20px;border-radius:50%;background:var(--white)}
.links li{list-style:none;font-size:10px;margin-bottom:14px}
.thumbs{display:grid;grid-template-columns:repeat(3,72px);gap:8px}
.thumbs i{height:54px;border-radius:0 10px 0 10px}
.legal{position:absolute;left:154px;right:150px;bottom:16px;display:flex;justify-content:space-between;font-size:9px}
.legal .hl{color:var(--cyan)}
</style>
</head>
<body>

<header class="hero">
  <div class="topbar">
    <div class="brand">
      <span class="brand-mark"></span>
      <div><div class="brand-name">QUILL</div><div class="brand-tag">MARKETING VIDEOS MADE FOR YOU</div></div>
    </div>
    <nav class="nav">
      <a>Home</a><a class="active">How It Works</a><a>Examples</a><a>Faq</a><a>Contact Us</a><a>Pricing</a>
      <span class="auth"><span class="login">Login</span><span>Sign up</span></span>
    </nav>
  </div>
  <div class="hero-copy">
    <h1>Attention Grabbing<br><em>VIRAL</em> Type Video Adds</h1>
    <div class="hero-cta"><a class="btn">Get Free Video Mockup Now!</a><span>All delivered in <u>24 hours</u></span></div>
  </div>
  <div class="hero-photo" role="img" aria-label="Woman sitting on a boat on a lake"></div>
  <div class="play" style="left:618px;top:306px"></div>
  <div class="band"></div>
  <svg class="chevrons" width="30" height="60" viewBox="0 0 30 60" aria-hidden="true">
    <g fill="none" stroke="#5b6fa8" stroke-width="3"><path d="M5 5l10 9 10-9"/><path d="M5 20l10 9 10-9"/><path d="M5 35l10 9 10-9"/><path d="M5 50l10 9 10-9"/></g>
  </svg>
</header>

<section class="promote">
  <div class="collage">
    <div class="a" role="img" aria-label="Two women in matching red dresses"></div>
    <div class="b" role="img" aria-label="Woman in a white dress on stairs"></div>
    <div class="c"><i>+</i></div>
    <div class="play"></div>
  </div>
  <div class="block">
    <span class="flag"></span>
    <h2>Promote Anything</h2>
    <div class="sub">Anywhere on the web</div>
    <p>For less than the cost and time of a DIY video maker software, we will make you one of these <b>promotional marketing videos</b> that will make your business stand out from the competition.</p>
    <a class="btn">Get Free Demo</a>
  </div>
</section>

<section class="award">
  <div class="block">
    <span class="flag"></span>
    <h2>Award Winning Marketing Videos</h2>
    <div class="sub">We create award winning promotional videos</div>
    <p>Stop using static images with Friendline, Snapframe or any other social advertising platform! Turn them into <b>VIDEO ADS</b> and get <b>higher conversion rates</b> instantly.</p>
    <a class="btn">Get Free Demo</a>
  </div>
  <div class="social-cluster" role="img" aria-label="Group of social video platform tiles"></div>
</section>

<div class="band" style="top:1635px"></div>

<section class="portfolio">
  <h2 class="section-title">Our Video Portfolio</h2>
  <div class="cards">
    <div class="pcard">
      <div class="thumb" role="img" aria-label="Smiling man in a shirt" style="background:linear-gradient(135deg,#8fb0c9,#d9b08c 60%,#3b5d8a)"><i class="heart"></i><i class="share"></i><span>WE JUST BOOSTED SALES BY 35%</span><div class="play"></div></div>
      <h3>Marketing Promo 1</h3>
    </div>
    <div class="pcard">
      <div class="thumb" role="img" aria-label="Hands counting banknotes" style="background:linear-gradient(135deg,#4b5e4a,#9aa58a 55%,#2b3338)"><i class="heart"></i><i class="share"></i><span>WHAT WILL YOU DO WITH ALL THE MONEY YOU MAKE?</span><div class="play"></div></div>
      <h3>Marketing Promo 2</h3>
    </div>
    <div class="pcard">
      <div class="thumb" role="img" aria-label="Camera operator filming outdoors" style="background:linear-gradient(135deg,#7b9ac0,#c8d3de 50%,#33425a)"><i class="heart"></i><i class="share"></i><span>DO WHAT YOU DO BEST</span><div class="play"></div></div>
      <h3>Marketing Promo 2</h3>
    </div>
  </div>
  <div class="center"><a class="btn plain">Show All Categories</a></div>
</section>

<div class="band" style="top:2200px"></div>

<section class="features">
  <h2 class="section-title">Our Awesome Features</h2>
  <div class="fgrid">
    <div class="fcard"><h3>Done For You</h3><div class="tag">You don't lift a finger</div><p>We make it super affordable and we DO IT ALL FOR YOU! You'll receive a fully packaged product.</p><span class="more">READ MORE</span><i class="ico"></i></div>
    <div class="fcard dark"><h3>Premium Content</h3><div class="tag">Your business will look super high end and professional</div><p>We have access to millions of premium video clips, fully packaged by Award Winning Videographers.</p><span class="more">READ MORE</span><i class="ico"></i></div>
    <div class="fcard"><h3>Fully licensed to you</h3><div class="tag">You own all the videos-consider them yours!</div><p>The videos are your property and come with a lifetime license for unlimited sharing and use.</p><span class="more">READ MORE</span><i class="ico"></i></div>
    <div class="fcard"><h3>Perfect length for videos</h3><div class="tag">Stand out from the crowd from video marketing</div><p>Our Marketing Videos range from 20 seconds up to 30 seconds in length. These are the sweet spot.</p><span class="more">READ MORE</span><i class="ico"></i></div>
    <div class="fcard"><h3>Social video cover</h3><div class="tag">Wow customers with beautiful designed social covers</div><p>We can convert any video to a Friendline Video Cover for your business page.</p><span class="more">READ MORE</span><i class="ico"></i></div>
    <div class="fcard"><h3>Best support</h3><div class="tag">We are available to you at all times for any support!</div><p>The videos are your property and come with a lifetime license for unlimited sharing and use.</p><span class="more">READ MORE</span><i class="ico"></i></div>
  </div>
  <div class="center"><a class="btn">Get Free Demo</a></div>
</section>

<section class="sizes">
  <h2 class="section-title">Video Sizes Available</h2>
  <div class="srow" style="top:130px;height:160px">
    <p class="stext"><b>Wide Screen Videos</b> – This size is a standard video size that works best for posting to all platforms on the web <span class="hl">(1280x720)</span>. Included with all video purchases.</p>
    <div class="shot" style="height:155px;background:linear-gradient(135deg,#f0c23b,#d9472f 60%,#2a78c7)" role="img" aria-label="Colourful street art scene"><span>LIVE YOUR PASSION</span></div>
    <div class="shot" style="height:155px;background:linear-gradient(135deg,#c9b79c,#5c6a5a)" role="img" aria-label="Two people outdoors"></div>
    <div class="shot" style="height:155px;background:linear-gradient(135deg,#3e8bd1,#f2c94c 55%,#2a3d6e)" role="img" aria-label="Person with a bright mask"><span>BE ANONYMOUS</span></div>
  </div>
  <div class="srow" style="top:316px;height:210px">
    <div class="shot" style="height:205px;background:linear-gradient(135deg,#e04f6d,#f2a3b6 50%,#3c7ad6)" role="img" aria-label="Person holding a pay what you want sign"></div>
    <div class="shot" style="height:205px;background:linear-gradient(135deg,#3d5a7a,#c45a5a 55%,#5a6b7d)" role="img" aria-label="Woman with question marks"></div>
    <div class="shot" style="height:205px;background:linear-gradient(135deg,#cba67e,#7c5a44 60%,#3a3a4a)" role="img" aria-label="Friends laughing together"><span>ENJOY LIFE</span></div>
    <p class="stext"><b>Square Videos</b> that work best on FRIENDLINE <span class="hl">(Square is 1080 X 1080)</span>. Convert any video to this size for an additional fee of <b>$29</b>.</p>
  </div>
  <div class="srow" style="top:552px;height:340px">
    <p class="stext"><b>Vertical Videos</b> that work best on STORIES for Friendline, Snapframe and Blinkcast <span class="hl">(1080 X 1920)</span>. Convert any video to this size for an additional fee of <b>$29</b>.</p>
    <div class="shot" style="height:335px;background:linear-gradient(180deg,#e9b8b4,#3a3a44 60%,#7b8aa6)" role="img" aria-label="Woman in a graphic t-shirt"></div>
    <div class="shot" style="height:335px;background:linear-gradient(180deg,#f3c07a,#d46a3c 50%,#2f2f3a)" role="img" aria-label="Woman at a holiday resort"><span>HOLIDAY</span></div>
    <div class="shot" style="height:335px;background:linear-gradient(180deg,#d9e4ef,#c63a3a 55%,#6b7f96)" role="img" aria-label="Athlete running on a track"><span>ATHLETE</span></div>
  </div>
  <div class="center"><a class="btn">Get Free Demo</a></div>
</section>

<div class="band" style="top:4040px"></div>

<footer class="footer">
  <div class="fcol" style="left:154px;width:300px">
    <div class="brand"><span class="brand-mark"></span><div><div class="brand-name">QUILL</div><div class="brand-tag">MARKETING VIDEOS MADE FOR YOU</div></div></div>
    <p class="strong">CREATED BY A MARKETER FOR MARKETERS</p>
    <p>With Quill, you simply tell us how or what you want to promote and we will have your video all finished as soon as <span class="hl">24 hours!</span></p>
    <div class="dots"><i></i><i></i><i></i><i></i><i></i></div>
  </div>
  <div class="fcol" style="left:548px">
    <h4>QUICK LINKS</h4>
    <ul class="links"><li>How It Works</li><li>Term Of Service</li><li>Privacy Policy</li><li>Custom Policy</li></ul>
  </div>
  <div class="fcol" style="left:775px">
    <h4>LATEST PROMO VIDEOS</h4>
    <div class="thumbs">
      <i role="img" aria-label="Promo video still" style="background:#6c86a8"></i>
      <i role="img" aria-label="Promo video still" style="background:#8a7a6a"></i>
      <i role="img" aria-label="Promo video still" style="background:#4e5a6e"></i>
      <i role="img" aria-label="Promo video still" style="background:#a08c7a"></i>
      <i role="img" aria-label="Promo video still" style="background:#5d7394"></i>
      <i role="img" aria-label="Promo video still" style="background:#7d6a5e"></i>
    </div>
  </div>
  <div class="legal"><span>Copyright @ <span class="hl">quillhavenfilmworks</span></span><span class="hl">Terms of Use &nbsp;|&nbsp; Privacy Policy</span></div>
</footer>

</body>
</html>
```